Website design for commercial and residential security company

we're looking to see some new designs for an established company with no website.

homepage and one inner page

here is a link to the homepage content, sitemap, logo and more.
https://files.trovelink-share.net/folders/7QmzKpw3RtvxnLa9eHs2YcdJfuoPb?view=open

call to action should be Request A Quote

if you have any questions please send them to us asap

thank you

Number of Pages Required

1 page

Font styles to use
Sans Serif

```html
<!DOCTYPE html>
<html lang="en">
<head>
<meta charset="utf-8">
<title>Silver Beacon Business Solutions</title>
<link rel="stylesheet" href="https://fonts.googleapis.com/css2?family=Josefin+Sans:wght@400;600;700&family=Lato:wght@400;700&display=swap">
<style>
:root{
  --navy:#0a1a5c;
  --navy-deep:#06103d;
  --gold:#d4b13a;
  --white:#ffffff;
  --ink:#1b1b1b;
  --grey-bg:#eeecec;
  --field:#e4e1e1;
  --footer:#262626;
  --muted:#bdbdbd;
}
*{box-sizing:border-box;margin:0;padding:0}
html,body{width:1200px;height:3350px;overflow:hidden;background:var(--white)}
body{font-family:"Lato",sans-serif;color:var(--ink)}
.page{position:relative;width:1200px;height:3350px}
section,footer{position:relative;width:1200px;overflow:hidden}

/* header + hero */
.hero{height:720px;background:radial-gradient(ellipse at 70% 45%,#14307f 0%,var(--navy) 45%,var(--navy-deep) 100%)}
.brand{position:absolute;font-family:"Josefin Sans",sans-serif;font-weight:700;color:var(--gold);letter-spacing:1px}
.hero .brand{left:220px;top:36px;font-size:22px;line-height:1.05}
.nav{position:absolute;top:44px;left:455px;font-family:"Josefin Sans",sans-serif;font-size:11px;font-weight:600;color:var(--white);text-transform:uppercase}
.nav a{color:inherit;text-decoration:none;position:absolute;white-space:nowrap}
.nav .active{color:var(--gold)}
.btn-quote-top{position:absolute;left:875px;top:33px;width:104px;height:30px;background:var(--gold);color:var(--white);font-family:"Josefin Sans",sans-serif;font-size:10px;font-weight:700;display:flex;align-items:center;justify-content:center;border-radius:2px}
.hero-copy{position:absolute;left:220px;top:205px;width:480px;color:var(--white);font-family:"Josefin Sans",sans-serif;z-index:2}
.hero-copy .welcome{font-size:30px;font-weight:400}
.hero-copy .name{font-size:50px;font-weight:700;color:var(--gold);line-height:1;margin-top:14px;white-space:nowrap}
.hero-copy .sub{font-size:34px;font-weight:700;margin-top:8px;white-space:nowrap}
.hero-copy .tag{font-size:12px;font-weight:600;margin-top:16px;white-space:nowrap}
.hero-copy .tag b{color:var(--gold)}
.btn-outline{display:inline-flex;align-items:center;justify-content:center;width:140px;height:38px;border:1px solid var(--white);font-size:12px;margin-top:30px;border-radius:2px}
.dots{display:flex;gap:12px;margin-top:36px}
.dots i{width:11px;height:11px;border:1.5px solid var(--white);border-radius:50%}
.dots i.on{background:var(--gold);border-color:var(--gold)}
.hero-visual{position:absolute;left:720px;top:110px;width:330px;height:480px;border-radius:40px;background:radial-gradient(circle at 45% 40%,#d9e0ee 0%,#8c9bbf 45%,rgba(20,48,127,0) 75%)}
.arrow{position:absolute;top:420px}
.hero-curve{position:absolute;left:0;bottom:0}

/* about */
.about{height:430px;background:var(--white)}
.about-visual{position:absolute;left:220px;top:30px;width:315px;height:270px;background:linear-gradient(135deg,#9aa3ad,#3b4450 55%,#2fb4d9);clip-path:polygon(25% 0,75% 0,100% 50%,75% 100%,25% 100%,0 50%)}
.about-copy{position:absolute;left:600px;top:65px;width:390px}
.eyebrow{font-family:"Josefin Sans",sans-serif;color:var(--gold);font-size:19px}
.about-copy h2{font-family:"Josefin Sans",sans-serif;font-size:18px;font-weight:700;margin-top:4px;white-space:nowrap}
.about-copy p{font-size:9.5px;line-height:1.8;margin-top:20px;color:#333}
.btn-dark{display:inline-flex;align-items:center;justify-content:center;width:96px;height:36px;background:var(--ink);color:var(--white);font-size:10px;margin-top:18px;border-radius:2px}

/* solutions */
.solutions{height:660px;background:var(--grey-bg)}
.section-title{font-family:"Josefin Sans",sans-serif;font-weight:700;font-size:32px;text-align:center}
.solutions .section-title{padding-top:58px}
.rule{width:42px;height:2px;background:var(--gold);margin:10px auto 0}
.toggle{position:absolute;left:221px;top:138px;width:758px;height:64px;border-radius:32px;background:var(--ink);display:flex;overflow:hidden;font-family:"Josefin Sans",sans-serif;font-weight:700;font-size:28px}
.toggle span{flex:1;display:flex;align-items:center;justify-content:center;color:var(--gold)}
.toggle .on{background:var(--gold);color:var(--ink);border-radius:32px}
.cards{position:absolute;left:221px;top:232px;display:flex;gap:28px}
.card{width:169px;text-align:center}
.card .thumb{height:184px;border-radius:8px}
.card h3{font-family:"Josefin Sans",sans-serif;font-size:19px;font-weight:700;margin-top:20px;white-space:nowrap}
.card h3.active{color:var(--gold)}
.pager{position:absolute;top:530px;left:0;width:100%;display:flex;justify-content:center;gap:10px}
.pager i{width:13px;height:13px;border-radius:50%;background:#9a9a9a}
.pager i.on{background:var(--ink)}

/* resources */
.resources{height:480px;background:linear-gradient(180deg,#0a0d18 0%,#0f1a36 60%,#1f3a66 85%,#0d1630 100%);color:var(--white);text-align:center}
.resources .section-title{padding-top:62px;color:var(--white)}
.resources p{width:760px;margin:30px auto 0;font-family:"Josefin Sans",sans-serif;font-size:20px;line-height:1.8}
.res-actions{display:flex;justify-content:center;gap:12px;margin-top:30px}
.res-actions span{width:96px;height:38px;display:flex;align-items:center;justify-content:center;font-size:11px;border-radius:2px}
.res-actions .gold{background:var(--gold);color:var(--white)}
.res-actions .light{background:var(--white);color:var(--ink)}

/* contact */
.contact{height:600px;background:var(--grey-bg)}
.contact-photo{position:absolute;left:221px;top:70px;width:330px;height:530px;background:linear-gradient(180deg,#d8d2cd 0%,#8a7a6b 45%,#4f4b47 100%);border-radius:140px 140px 0 0}
.tablet{position:absolute;left:636px;top:95px;width:343px;height:465px;border:4px solid #333;border-radius:14px;background:#fdfdfd;padding:18px 14px}
.tablet h2{font-family:"Josefin Sans",sans-serif;font-size:34px;font-weight:700;text-align:center}
.field{height:40px;background:var(--field);margin-top:14px;font-size:9px;padding:12px 14px;color:#555}
.field.msg{height:86px}
.submit{height:40px;background:var(--gold);color:var(--white);font-size:9px;font-weight:700;display:flex;align-items:center;justify-content:center;margin-top:18px}
.home-key{position:absolute;left:50%;bottom:10px;width:44px;height:10px;margin-left:-22px;background:#333;border-radius:5px}

/* footer */
.site-footer{height:460px;background:var(--footer);color:var(--white);text-align:center}
.site-footer .brand{position:static;display:block;padding-top:72px;font-size:40px}
.foot-nav{display:flex;justify-content:center;margin-top:72px;font-size:11px}
.foot-nav a{color:var(--white);text-decoration:none;padding:0 50px;border-right:1px solid var(--white)}
.foot-nav a:last-child{border-right:0}
.foot-nav a.active{color:var(--gold)}
.foot-rule{width:758px;height:1px;background:#555;margin:26px auto 0}
.foot-contact{display:flex;justify-content:center;gap:52px;margin-top:26px;font-size:11px;align-items:center;text-align:left}
.foot-contact div{display:flex;align-items:center;gap:8px}
.social{display:flex;justify-content:center;gap:8px;margin-top:30px}
.social i{width:28px;height:28px;border:1.5px solid var(--white);border-radius:50%}
.social i.on{border-color:var(--gold)}
.copyright{font-size:9px;margin-top:26px;color:var(--muted)}
</style>
</head>
<body>
<div class="page">

<section class="hero">
  <div class="brand">SILVER BEACON<br><span style="font-size:11px;letter-spacing:3px">BUSINESS SOLUTIONS</span></div>
  <nav class="nav">
    <a class="active" style="left:5px">Home</a>
    <a style="left:59px">About Us</a>
    <a style="left:145px">Solutions &#8964;</a>
    <a style="left:238px">Resources &#8964;</a>
    <a style="left:336px">Contact</a>
  </nav>
  <div class="btn-quote-top">REQUEST A QUOTE</div>

  <div class="hero-visual" role="img" aria-label="Security camera on wall mount"></div>

  <div class="hero-copy">
    <div class="welcome">WELCOME TO</div>
    <div class="name">SILVER BEACON</div>
    <div class="sub">BUSINESS SOLUTIONS</div>
    <div class="tag">WE PROVIDE <b>SECURITY</b>, <b>AUDIO/VIDEO</b>, AND <b>AUTOMATION</b></div>
    <div class="btn-outline">REQUEST A QUOTE</div>
    <div class="dots"><i></i><i></i><i class="on"></i><i></i><i></i></div>
  </div>

  <svg class="arrow" style="left:30px" width="44" height="44" viewBox="0 0 44 44"><circle cx="22" cy="22" r="20" fill="none" stroke="#2b4a9a" stroke-width="2"/><path d="M30 22H14M20 16l-6 6 6 6" fill="none" stroke="#2b4a9a" stroke-width="2"/></svg>
  <svg class="arrow" style="left:1126px" width="44" height="44" viewBox="0 0 44 44"><circle cx="22" cy="22" r="20" fill="none" stroke="#fff" stroke-width="2"/><path d="M14 22h16M24 16l6 6-6 6" fill="none" stroke="#fff" stroke-width="2"/></svg>

  <svg class="hero-curve" width="1200" height="40" viewBox="0 0 1200 40" preserveAspectRatio="none"><path d="M0 40 Q600 -18 1200 40 Z" fill="#fff"/></svg>
</section>

<section class="about">
  <div class="about-visual" role="img" aria-label="Collage of keypad, security camera and smartphone app"></div>
  <div class="about-copy">
    <div class="eyebrow">ABOUT US</div>
    <h2>SILVER BEACON BUSINESS SOLUTIONS</h2>
    <p>To provide our customers with comprehensive security, audio/video, and automation with top notch customer service. We Ensure Security with Smart Tools. The graded security measures from Silver Beacon Business Solutions ensure the safety of both residential and commercial property. We provide a wide range of Residential and Commercial Security Solutions.</p>
    <div class="btn-dark">READ MORE</div>
  </div>
</section>

<section class="solutions">
  <h2 class="section-title">SOLUTIONS</h2>
  <div class="rule"></div>
  <div class="toggle"><span class="on">COMMERCIAL</span><span>RESIDENTIAL</span></div>
  <div class="cards">
    <div class="card"><div class="thumb" role="img" aria-label="CCTV dome camera on brick wall" style="background:linear-gradient(160deg,#b8a49a,#6d6560)"></div><h3>CCTV</h3></div>
    <div class="card"><div class="thumb" role="img" aria-label="Person working at access control monitor" style="background:linear-gradient(160deg,#4d5a4a,#1e2320)"></div><h3 class="active">ACCESS CONTROL</h3></div>
    <div class="card"><div class="thumb" role="img" aria-label="Red alarm light on metal surface" style="background:linear-gradient(160deg,#5a5f66,#2a2c30)"></div><h3>ALARM</h3></div>
    <div class="card"><div class="thumb" role="img" aria-label="Laptop screen with padlock graphic" style="background:linear-gradient(160deg,#2346a8,#c9c9c9)"></div><h3>AUDIO / VIDEO</h3></div>
  </div>
  <div class="pager"><i></i><i class="on"></i></div>
</section>

<section class="resources" role="img" aria-label="City skyline at night behind resources text">
  <h2 class="section-title">RESOURCES</h2>
  <p>At vero eos et accusamus et iusto odio dignissimos ducimus qui blanditiis praesentium voluptatum deleniti atque corrupti quos dolores et quas molestias excepturi sint occaecati cupiditate non provident, similique sunt in culpa qui officia deserunt mollitia animi, id est laborum et dolorum fuga.</p>
  <div class="res-actions"><span class="gold">PACKAGES</span><span class="light">SPECIALS</span></div>
</section>

<section class="contact">
  <div class="contact-photo" role="img" aria-label="Smiling customer holding phone and coffee"></div>
  <div class="tablet">
    <h2>GET IN TOUCH</h2>
    <div class="field">NAME</div>
    <div class="field">PHONE</div>
    <div class="field">E-MAIL</div>
    <div class="field msg">MESSAGE</div>
    <div class="submit">SUBMIT &#10148;</div>
    <div class="home-key"></div>
  </div>
</section>

<footer class="site-footer">
  <div class="brand">SILVER BEACON</div>
  <nav class="foot-nav">
    <a class="active">HOME</a><a>ABOUT US</a><a>SOLUTIONS</a><a>RESOURCES</a><a>CONTACT</a>
  </nav>
  <div class="foot-rule"></div>
  <div class="foot-contact">
    <div><svg width="14" height="14" viewBox="0 0 24 24"><path d="M6.6 10.8a15 15 0 006.6 6.6l2.2-2.2a1 1 0 011-.25 11.4 11.4 0 003.6.57 1 1 0 011 1V20a1 1 0 01-1 1A17 17 0 013 4a1 1 0 011-1h3.5a1 1 0 011 1c0 1.25.2 2.45.57 3.6a1 1 0 01-.25 1z" fill="#d4b13a"/></svg>(555) - 010 - 274</div>
    <div><svg width="14" height="16" viewBox="0 0 24 28"><path d="M12 0a9 9 0 00-9 9c0 7 9 19 9 19s9-12 9-19a9 9 0 00-9-9zm0 12a3 3 0 110-6 3 3 0 010 6z" fill="#d4b13a"/></svg><span>Head Office Address<br>123 Lorem ipsum Street, Country</span></div>
    <div><svg width="16" height="12" viewBox="0 0 24 18"><rect width="24" height="18" rx="2" fill="#d4b13a"/><path d="M1 2l11 8 11-8" fill="none" stroke="#262626" stroke-width="2"/></svg>hello@silverbeacon-mail.com</div>
  </div>
  <div class="social"><i></i><i class="on"></i><i></i></div>
  <div class="copyright">Copyright 2021 SILVER BEACON BUSINESS SOLUTIONS. All Rights Are Reserved.</div>
</footer>

</div>
</body>
</html>
```